HOT TUB - SPAS service needs an business card

I need an business for my company who his specialise in a maintenance,water treatment and cleaning of Hot Tub - Spas for commercial and residential customers. The company operate mainly in the ski resort of Chamonix, Megève and St Gervais. The final product should communicate pure water, cleanest and professional for luxury property's.
I have upload a logo but any improvement on it is welcome.(color,size, details etc..) or any other idea. Thank you
Company Name: 58 SPAS
My name: Mathis Darrouzet
Email: mathdarr@mailvexo.net
Tel: +33 (0)6 71 52 08 93
Description to be on the card in french(first langage) and in English:
- Spas service
- Entretien, traitement eau, nettoyage.
- Maintenance, water treatment, cleaning.

```html
<!DOCTYPE html>
<html lang="fr">
<head>
<meta charset="utf-8">
<title>58 SPAS – Business Card</title>
<link rel="stylesheet" href="https://fonts.googleapis.com/css2?family=Source+Sans+3:wght@400;600;700&display=swap">
<style>
  :root {
    --page-bg: #eef1f4;
    --water-light: #4fb4f2;
    --water-mid: #2b9be8;
    --water-deep: #1478d2;
    --wave-dark: #0f68c4;
    --wave-line: #3fa6ee;
    --ink: #ffffff;
    --emblem-soft: rgba(255, 255, 255, 0.08);
    --emblem-bright: rgba(255, 255, 255, 0.22);
    --card-radius: 34px;
  }
  * { box-sizing: border-box; margin: 0; padding: 0; }
  html, body {
    width: 1200px;
    height: 1150px;
    overflow: hidden;
    background: var(--page-bg);
    font-family: "Source Sans 3", "Myriad Pro", Arial, sans-serif;
    color: var(--ink);
  }
  .canvas { position: relative; width: 1200px; height: 1150px; }

  .card {
    position: absolute;
    width: 847px;
    height: 484px;
    border-radius: var(--card-radius);
    overflow: hidden;
    box-shadow: 0 4px 14px rgba(20, 60, 110, 0.18);
  }
  .card--front { left: 295px; top: 60px; }
  .card--back  { left: 48px;  top: 599px; }

  .water-texture {
    position: absolute;
    inset: 0;
    background:
      radial-gradient(ellipse at 30% 20%, rgba(255,255,255,0.18), transparent 60%),
      linear-gradient(160deg, var(--water-light) 0%, var(--water-mid) 55%, var(--water-deep) 100%);
  }
  .wave { position: absolute; inset: 0; width: 100%; height: 100%; }

  .emblem {
    position: absolute;
    border-radius: 6px;
    background: linear-gradient(180deg, var(--emblem-soft) 0%, var(--emblem-bright) 100%);
  }
  .card--front .emblem { left: 119px; top: 55px; width: 534px; height: 151px; }
  .card--back .emblem  { left: 104px; top: 99px; width: 653px; height: 175px; }

  .company-name {
    position: absolute;
    left: 118px; top: 210px;
    font-size: 38px;
    font-weight: 600;
    line-height: 1.2;
  }
  .person-name {
    position: absolute;
    left: 118px; top: 310px;
    font-size: 34px;
    font-weight: 700;
    line-height: 1.2;
  }
  .contact {
    position: absolute;
    right: 34px;
    display: flex;
    align-items: center;
    gap: 12px;
    font-size: 27px;
    font-weight: 400;
    line-height: 1.2;
  }
  .contact--phone { top: 378px; }
  .contact--email { top: 428px; }
  .contact__icon { width: 24px; height: 24px; flex: none; }

  .services {
    position: absolute;
    left: 0; right: 0; top: 338px;
    text-align: center;
  }
  .services__title {
    font-size: 29px;
    font-weight: 600;
    line-height: 40px;
    margin-bottom: 8px;
  }
  .services__line {
    font-size: 29px;
    font-weight: 400;
    line-height: 40px;
  }
</style>
</head>
<body>
<div class="canvas">

  <section class="card card--front">
    <div class="water-texture" role="img" aria-label="Water droplets on a blue surface"></div>
    <svg class="wave" viewBox="0 0 847 484" preserveAspectRatio="none" aria-hidden="true">
      <path d="M0 310 C 160 330, 260 420, 430 400 C 590 380, 690 300, 847 300 L847 484 L0 484 Z" fill="var(--wave-dark)"/>
      <path d="M45 432 C 200 470, 330 470, 470 430 C 610 390, 720 300, 847 312" fill="none" stroke="var(--wave-line)" stroke-width="10"/>
    </svg>
    <div class="emblem" role="img" aria-label="Company emblem: line drawing of mountains, a chalet and a spa"></div>
    <div class="company-name">58 SPAS</div>
    <div class="person-name">Mathis Darrouzet</div>
    <div class="contact contact--phone">
      <svg class="contact__icon" viewBox="0 0 24 24" aria-hidden="true">
        <circle cx="12" cy="12" r="10.5" fill="none" stroke="#fff" stroke-width="1.6"/>
        <path d="M9 6.5 C7 8.5 7.5 13 10 15.5 C12.5 18 15.5 18 17 16.5 L15 14.3 L13.6 15 C12 14 10.3 12.2 9.5 10.5 L10.3 9 Z" fill="#fff"/>
      </svg>
      <span>+33 (0)6 71 52 08 93</span>
    </div>
    <div class="contact contact--email">
      <svg class="contact__icon" viewBox="0 0 24 24" aria-hidden="true">
        <rect x="1.5" y="6" width="21" height="13" rx="1.5" fill="#fff"/>
        <path d="M2 7 L12 14 L22 7" fill="none" stroke="var(--water-deep)" stroke-width="1.6"/>
      </svg>
      <span>mathdarr@mailvexo.net</span>
    </div>
  </section>

  <section class="card card--back">
    <div class="water-texture" role="img" aria-label="Water droplets on a blue surface"></div>
    <div class="emblem" role="img" aria-label="Company emblem: line drawing of mountains, a chalet and a spa"></div>
    <div class="services">
      <h2 class="services__title">SPAS SERVICES</h2>
      <p class="services__line">•Entretien &nbsp;•traitement eau &nbsp;•nettoyage</p>
      <p class="services__line">•Maintenance &nbsp;•water treatment &nbsp;•cleaning.</p>
    </div>
  </section>

</div>
</body>
</html>
```